www.gopluvo.com.au Product Catalogue

I require the design of a product catalogue to promote the products that I provide.

Sizing: A5 booklet or DL size folded brochure double sided(A4)

The catalogue will be used to promote a range of tours & adventure activities.

The catalogue needs to use high gloss full color and be like a Travel brochure.

The company name is www.gopluvo.com.au

"We are the Tarrinvale' Adventure Booking Store"

Contact: info@gopluvo.com.au

I have a logo which I wish to use on the front of the brochure and through out.

the website address is www.gopluvo.com.au
We provide Tours & Adventure Activities in the Shoalhaven Coast region on the NSW South Coast Australia.

HERE IS A LIST OF THE TYPES OF PRODUCTS.

BOAT HIRE
COACH TOUR
TEMPLE TOUR
KANGAROO VALLEY TOUR
WINERY TOUR
FOOD & WINE TOUR
SHOALHAVEN SCENIC SIGHTS TOUR
JERVIS BAY DAY TOUR
GRAND PACIFIC DRIVE TOUR
ABORIGINAL CULTURE EXPERIENCE
HARLEY TOUR
SAILING CRUISE
RIVER CRUISE
WHALE/DOLPHIN CRUISE
SCENIC FLIGHT
SKYDIVING
WAKEBOARDING/TUBING/WATERSKIING
PADDLE BOARDING
LEARN TO SURF
KAYAKING KANGAROO VALLEY
MUSEUM
HISTORICAL SOCIETY TOURS
GHOST WALK
TREKKING
BUSH WALKING
ROCK CLIMBING
FISHING CHARTERS

We provide Online, Retail booking services as well as Gift Certificates/Vouchers.

Project Deadline Extended Reason: i HAVE DECIDED TO EXTEND THE DEADLINE FOR MY PROJECT TO ALLOW EACH DESIGNER A LITTLE MORE TIME TO COMPLETE THEIR DESIGN WORK. GOOD LUCK. Added Friday, November 28, 2014

Target Market(s)

Families, Couples, Budget Traveler

Industry/Entity Type

It Company

Font styles to use
Serif

Requirements
Must have
• Each product must have atleast 1 image.
• Please note that some of the images may be duplicates, so all I require will be the use of the image once.. not every image. Not all images are required or suitable for use, which I undestand. If you require any additional images please message me and I will see if I can provide something better for the brochure.

```html
<!DOCTYPE html>
<html lang="en">
<head>
<meta charset="utf-8">
<title>gopluvo – Catalogue Cover Spread</title>
<link rel="stylesheet" href="https://fonts.googleapis.com/css2?family=Marcellus&display=swap">
<style>
  :root {
    --stage: #2b2b2b;
    --ink: #111111;
    --paper-light: #ffffff;
    --paper-shade: #c9c9c9;
    --sky-top: #5f93d6;
    --sky-low: #bcd6ee;
    --sea-deep: #0f3f86;
    --sea-shallow: #2fc3c9;
    --rock: #b8a680;
    --bush: #5d7a3e;
  }
  * { box-sizing: border-box; margin: 0; padding: 0; }
  html, body {
    width: 1200px;
    height: 1085px;
    overflow: hidden;
    background: var(--stage);
  }
  .spread {
    position: absolute;
    left: 62px;
    top: 162px;
    width: 1076px;
    height: 760px;
    display: flex;
    box-shadow: 0 18px 40px rgba(0,0,0,.55);
  }
  .page {
    position: relative;
    width: 538px;
    height: 760px;
    font-family: "Marcellus", "Times New Roman", serif;
    color: var(--ink);
  }
  /* Back cover */
  .back-cover {
    background: linear-gradient(100deg, var(--paper-shade) 0%, #ececec 28%, var(--paper-light) 55%, #f1f1f1 100%);
  }
  .back-cover .brand {
    position: absolute;
    left: 0; right: 0;
    top: 530px;
    justify-content: center;
  }
  .contact-list {
    position: absolute;
    top: 610px;
    left: 0; right: 0;
    list-style: none;
    text-align: center;
    font-size: 15px;
    line-height: 24px;
  }
  .contact-list li {
    display: flex;
    justify-content: center;
    align-items: center;
    gap: 7px;
  }
  .contact-list svg { width: 12px; height: 12px; fill: var(--ink); }
  /* Front cover */
  .front-cover { overflow: hidden; }
  .cover-photo {
    position: absolute;
    inset: 0;
    background:
      linear-gradient(180deg,
        var(--sky-top) 0%,
        var(--sky-low) 38%,
        var(--bush) 44%,
        var(--sea-deep) 50%,
        var(--sea-deep) 60%,
        var(--sea-shallow) 68%,
        var(--rock) 76%,
        var(--bush) 100%);
  }
  .front-cover .brand {
    position: absolute;
    left: 0; right: 0;
    top: 60px;
    justify-content: center;
  }
  .cover-title {
    position: absolute;
    left: 0; right: 0;
    top: 150px;
    text-align: center;
    font-size: 31px;
    line-height: 40px;
    font-weight: 400;
  }
  .brand {
    display: flex;
    align-items: center;
    gap: 10px;
    font-size: 44px;
    line-height: 1;
    color: var(--ink);
  }
  .brand-dot {
    width: 16px; height: 16px;
    border-radius: 50%;
    background: var(--ink);
  }
</style>
</head>
<body>
  <main class="spread">
    <section class="page back-cover">
      <div class="brand"><span class="brand-dot"></span><span class="brand-name">gopluvo</span></div>
      <ul class="contact-list">
        <li>
          <svg viewBox="0 0 24 24" aria-hidden="true"><path d="M6.6 10.8a15.5 15.5 0 0 0 6.6 6.6l2.2-2.2a1 1 0 0 1 1-.25 11.4 11.4 0 0 0 3.6.57 1 1 0 0 1 1 1V20a1 1 0 0 1-1 1A17 17 0 0 1 3 4a1 1 0 0 1 1-1h3.5a1 1 0 0 1 1 1c0 1.25.2 2.45.57 3.57a1 1 0 0 1-.25 1z"/></svg>
          <span>02 - 5550 4172</span>
        </li>
        <li>
          <svg viewBox="0 0 24 24" aria-hidden="true"><path d="M2 5h20v14H2z M2 5l10 8 10-8" /></svg>
          <span>info@gopluvo.com.au</span>
        </li>
        <li>
          <svg viewBox="0 0 24 24" aria-hidden="true"><circle cx="12" cy="12" r="10"/></svg>
          <span>www.gopluvo.com.au</span>
        </li>
      </ul>
    </section>

    <section class="page front-cover">
      <div class="cover-photo" role="img" aria-label="Coastal photograph: turquoise bay framed by sandstone cliffs and bush, with a metal staircase leading down to the water"></div>
      <div class="brand"><span class="brand-dot"></span><span class="brand-name">gopluvo</span></div>
      <h1 class="cover-title">The Tarrinvale' Adventure<br>Booking Store</h1>
    </section>
  </main>
</body>
</html>
```